Flyer design for VIP membership

We need an A4 flyer design for our automotive workshop explaining and advertising to our customers about our VIP membership.

We are a modern and new workshop in New Zealand. I have attached our business card and another design for you to view. Along with company logo. Our colours are black, white and red.

Design needs to stand out and be easy to read.

Design must include the following wording:
___________________________________________________________________--

BLUESTONE TOTAL AUTOMOTIVE
VIP
FLEET VEHICLE SERVICING AND MAINTENANCE
Tradie?
Business owner?
Own 3 or more vehicles?
Become an Bluestone VIP member and receive:
• 10% off Vehicle Servicing and Mechanical Repairs
• 10% off Tyres
• Free basic vehicle exterior wash with every job
• Free puncture repairs
• Vehicle Delivery and Pick up
• Vehicle WOF, Service and Wheel Alignment reminders
• Given quick and first choice on all bookings and appointments
• Organise a tow truck to workshop for local break downs

If you’ve got a fleet of vehicles for your business, Bluestone can make it easy for you to stay on top of your servicing and maintenance schedules. We offer peace of mind motoring that ensures your vehicles are safe and reliable at cost effective prices.
Bluestone is your one stop automotive shop. We aim to make your automotive servicing and repairs as easy and painless as possible. We pride ourselves on excellent customer service and quality workmanship in a professional manner at competitive rates, using the latest technology and equipment.

Our services include:
• Vehicle Servicing
• All Mechanical Repairs
• Brakes, steering and suspension
• Transmission and cooling system servicing
• Warrant of fitness inspections
• Safety checks and pre-purchase inspections
• Tyres and wheel alignments
• Puncture repairs
• Mag wheels
• Vehicle Lowering and lift kits
• Automotive diagnostics
• Trailer repairs, maintenance and parts
• Automotive parts and supplies
• 4WD accessories
• Batteries
• And more
Contact us today to enquire about becoming an Bluestone VIP member.
Phone: 07 452 3917
Email: office@bluestoneautoworks.example.nz
Website: www.bluestoneautoworks.example.nz

```html
<!DOCTYPE html>
<html lang="en">
<head>
<meta charset="utf-8">
<title>Bluestone Total Automotive VIP Flyer</title>
<link href="https://fonts.googleapis.com/css2?family=Michroma&family=Montserrat:wght@400;500;600;700&display=swap" rel="stylesheet">
<style>
  :root {
    --red: #e31e24;
    --black: #0d0d0f;
    --charcoal: #1c1d21;
    --white: #ffffff;
    --ink: #1a1a1a;
    --grey: #bfbfbf;
    --backdrop: #d5d5d5;
  }
  * { margin: 0; padding: 0; box-sizing: border-box; }
  html, body { width: 703px; height: 1200px; overflow: hidden; background: var(--backdrop); }
  body { font-family: "Montserrat", sans-serif; color: var(--ink); }

  .flyer {
    position: absolute; left: 0; top: 103px;
    width: 703px; height: 993px;
    background: var(--white);
    overflow: hidden;
    box-shadow: 0 6px 18px rgba(0,0,0,.35);
  }
  .flyer-shapes { position: absolute; inset: 0; }

  .brand {
    position: absolute; left: 39px; top: 72px;
    font-family: "Michroma", sans-serif;
    font-size: 15px; line-height: 1.35; letter-spacing: 2px;
    color: var(--red);
  }
  .headline {
    position: absolute; left: 39px; top: 150px;
    font-family: "Michroma", sans-serif;
    font-size: 26px; line-height: 37px; letter-spacing: .5px;
  }
  .headline .accent { color: var(--red); display: block; }
  .headline .light { color: var(--white); display: block; }
  .subhead {
    position: absolute; left: 39px; top: 226px;
    font-family: "Michroma", sans-serif;
    font-size: 23px; line-height: 34px; color: var(--white);
    font-weight: 400;
  }

  .benefits-title {
    position: absolute; left: 38px; top: 430px;
    font-size: 18px; font-weight: 700; line-height: 21px; letter-spacing: .4px;
    color: var(--ink);
  }
  .benefits-title .accent { color: var(--red); display: block; }
  .rule { position: absolute; }
  .rule-grey { left: 39px; top: 485px; width: 224px; height: 1px; background: var(--grey); }
  .rule-red { left: 39px; top: 484px; width: 40px; height: 3px; background: var(--red); }
  .rule-white { left: 392px; top: 471px; width: 88px; height: 2px; background: var(--white); }

  .tick-list { list-style: none; position: absolute; }
  .tick-list li { position: absolute; left: 0; font-size: 12px; font-weight: 500; line-height: 14px; white-space: nowrap; }
  .tick-list svg { position: absolute; left: -27px; top: 0; width: 15px; height: 15px; }
  .benefits { left: 69px; top: 0; }
  .services { left: 426px; top: 0; color: var(--white); }
  .services li { font-weight: 600; }

  .contact-box {
    position: absolute; left: 37px; top: 825px; width: 283px; height: 82px;
    border: 1.5px solid var(--grey); border-radius: 6px;
    padding: 9px 16px; background: var(--white);
  }
  .contact-box p { font-size: 12.5px; font-weight: 700; line-height: 15px; }
  .contact-box .phone { font-size: 28px; font-weight: 700; color: var(--red); line-height: 34px; letter-spacing: .5px; }

  .services-title {
    position: absolute; left: 392px; top: 436px;
    font-size: 22px; font-weight: 700; color: var(--white); letter-spacing: .6px;
  }
  .services-title .accent { color: var(--red); }
  .and-more { position: absolute; left: 597px; top: 889px; font-size: 9px; color: var(--red); }

  .footer-contact { position: absolute; left: 288px; top: 940px; color: var(--white); font-size: 13.5px; font-weight: 500; line-height: 20px; }
  .footer-contact span { display: block; padding-left: 15px; position: relative; }
  .footer-contact svg { position: absolute; left: 0; top: 5px; width: 10px; height: 10px; }
  .follow { position: absolute; left: 585px; top: 951px; color: var(--white); font-size: 10px; display: flex; align-items: center; gap: 6px; }
  .follow i { display: inline-block; width: 16px; height: 16px; background: #3b5ba5; }
</style>
</head>
<body>
<svg width="0" height="0" style="position:absolute">
  <symbol id="tick" viewBox="0 0 16 16">
    <path d="M13.5 5.2A6.3 6.3 0 1 0 14 8" fill="none" stroke="#e31e24" stroke-width="1.4" stroke-linecap="round"/>
    <path d="M4.8 7.6l2.6 2.6 6.4-6.6" fill="none" stroke="#e31e24" stroke-width="1.5" stroke-linecap="round" stroke-linejoin="round"/>
  </symbol>
</svg>

<main class="flyer">
  <svg class="flyer-shapes" viewBox="0 0 703 993" width="703" height="993">
    <defs>
      <linearGradient id="headerTone" x1="0" y1="0" x2="1" y2="0.6">
        <stop offset="0" stop-color="#0f1013"/>
        <stop offset="0.55" stop-color="#2a2b30"/>
        <stop offset="0.8" stop-color="#4a4550"/>
        <stop offset="1" stop-color="#6b5a58"/>
      </linearGradient>
      <linearGradient id="panelTone" x1="0" y1="0" x2="0" y2="1">
        <stop offset="0" stop-color="#1a1a1d"/>
        <stop offset="1" stop-color="#0a0a0b"/>
      </linearGradient>
      <linearGradient id="whiteFade" x1="0" y1="0" x2="0" y2="1">
        <stop offset="0" stop-color="#e6e6e6"/>
        <stop offset="1" stop-color="#ffffff"/>
      </linearGradient>
    </defs>

    <rect x="0" y="330" width="703" height="140" fill="url(#whiteFade)"/>
    <polygon points="0,0 703,0 703,322 352,395 0,333" fill="url(#headerTone)" role="img" aria-label="Photo of a white delivery van parked in a workshop at dusk"/>

    <polygon points="0,328 240,378 226,386 0,340" fill="var(--red)"/>
    <polygon points="0,343 170,380 156,386 0,352" fill="var(--black)"/>
    <polygon points="703,325 703,337 470,389 458,381" fill="var(--red)"/>

    <polygon points="351,417 703,356 703,926 351,926" fill="url(#panelTone)"/>

    <rect x="0" y="955" width="240" height="4" fill="#9a9a9a"/>
    <rect x="0" y="961" width="225" height="4" fill="var(--black)"/>
    <polygon points="250,993 298,930 703,930 703,993" fill="var(--red)"/>
  </svg>

  <div class="brand">BLUESTONE<br>TOTAL AUTOMOTIVE</div>

  <h1 class="headline">
    <span class="accent">BLUESTONE TOTAL</span>
    <span class="light">AUTOMOTIVE VIP</span>
  </h1>
  <p class="subhead">Fleet Vehicle Servicing<br>And Maintenance</p>

  <h2 class="benefits-title">BECOME AN BLUESTONE<span class="accent">VIP MEMBER AND RECEIVE</span></h2>
  <div class="rule rule-grey"></div>
  <div class="rule rule-red"></div>

  <ul class="tick-list benefits">
    <li style="top:517px"><svg><use href="#tick"/></svg>10% off Vehicle Servicing and<br>Mechanical Repairs</li>
    <li style="top:560px"><svg><use href="#tick"/></svg>10% off Tyres</li>
    <li style="top:588px"><svg><use href="#tick"/></svg>Free basic vehicle exterior wash with<br>every job</li>
    <li style="top:631px"><svg><use href="#tick"/></svg>Free puncture repairs</li>
    <li style="top:659px"><svg><use href="#tick"/></svg>Vehicle Delivery and Pick up</li>
    <li style="top:687px"><svg><use href="#tick"/></svg>Vehicle WOF, Service and Wheel<br>Alignment reminders</li>
    <li style="top:730px"><svg><use href="#tick"/></svg>Given quick and first choice on all<br>bookings and appointments</li>
    <li style="top:772px"><svg><use href="#tick"/></svg>Organise a tow truck to workshop for<br>local break downs</li>
  </ul>

  <div class="contact-box">
    <p>Contact us today to enquire about<br>becoming an Bluestone VIP member.</p>
    <p class="phone">07 452 3917</p>
  </div>

  <h2 class="services-title">OUR <span class="accent">SERVICES</span></h2>
  <div class="rule rule-white"></div>

  <ul class="tick-list services">
    <li style="top:501px"><svg><use href="#tick"/></svg>Vehicle Servicing</li>
    <li style="top:527px"><svg><use href="#tick"/></svg>All Mechanical Repairs</li>
    <li style="top:553px"><svg><use href="#tick"/></svg>Brakes, steering and suspension</li>
    <li style="top:579px"><svg><use href="#tick"/></svg>Transmission and cooling system<br>servicing</li>
    <li style="top:618px"><svg><use href="#tick"/></svg>Warrant of fitness inspections</li>
    <li style="top:644px"><svg><use href="#tick"/></svg>Safety checks and pre-purchase<br>inspections</li>
    <li style="top:683px"><svg><use href="#tick"/></svg>Tyres and wheel alignments</li>
    <li style="top:709px"><svg><use href="#tick"/></svg>Puncture repairs</li>
    <li style="top:735px"><svg><use href="#tick"/></svg>Mag wheels</li>
    <li style="top:761px"><svg><use href="#tick"/></svg>Vehicle Lowering and lift kits</li>
    <li style="top:787px"><svg><use href="#tick"/></svg>Automotive diagnostics</li>
    <li style="top:813px"><svg><use href="#tick"/></svg>Trailer repairs, maintenance and parts</li>
    <li style="top:839px"><svg><use href="#tick"/></svg>Automotive parts and supplies</li>
    <li style="top:865px"><svg><use href="#tick"/></svg>4WD accessories</li>
    <li style="top:891px"><svg><use href="#tick"/></svg>Batteries</li>
  </ul>
  <span class="and-more">And more..</span>

  <div class="footer-contact">
    <span><svg viewBox="0 0 10 10"><circle cx="5" cy="5" r="4.2" fill="none" stroke="#fff" stroke-width="1"/><ellipse cx="5" cy="5" rx="1.8" ry="4.2" fill="none" stroke="#fff" stroke-width=".8"/><line x1=".8" y1="5" x2="9.2" y2="5" stroke="#fff" stroke-width=".8"/></svg>www.bluestoneautoworks.example.nz</span>
    <span><svg viewBox="0 0 10 10"><rect x=".5" y="2" width="9" height="6.5" fill="#fff"/><path d="M.5 2l4.5 3.6L9.5 2" fill="none" stroke="#e31e24" stroke-width=".9"/></svg>office@bluestoneautoworks.example.nz</span>
  </div>
  <div class="follow">Follow Us <i></i></div>
</main>
</body>
</html>
```